Buisness card

**Front Side:**

**[Your Company Logo]**
**Steadfast Upkeep Industrial**
*Keeping Your Equipment Running Smoothly*

**Contact Information:**
- **Name:** [darren Whitlow
- **Title:** [owner
- **Phone:** [8025196047
- **Email:** darren@sukrn.com

**Back Side:**

**Services Offered:**
- Routine Inspections
- Equipment Maintenance
- Emergency Repairs
- Consultation Services
- New installs
Tag line
Be proactive not reactive

```html
<!DOCTYPE html>
<html lang="en">
<head>
<meta charset="utf-8">
<title>Steadfast Upkeep Industrial – Business Card</title>
<link href="https://fonts.googleapis.com/css2?family=Montserrat:ital,wght@0,400;0,500;0,700;1,700&display=swap" rel="stylesheet">
<style>
  :root {
    --backdrop: #b5b5b5;
    --card: #f4f4f4;
    --ink: #333333;
    --ink-soft: #4a4a4a;
    --brand-navy: #1d3790;
    --rule: #555555;
  }
  * { box-sizing: border-box; margin: 0; padding: 0; }
  html, body {
    width: 1200px;
    height: 900px;
    overflow: hidden;
    background: var(--backdrop);
    font-family: "Montserrat", sans-serif;
    color: var(--ink);
  }
  .canvas { position: relative; width: 1200px; height: 900px; }
  .card {
    position: absolute;
    left: 395px;
    width: 410px;
    height: 236px;
    background: var(--card);
  }
  .card--back { top: 196px; }
  .card--front { top: 496px; }

  .brand {
    position: absolute;
    display: flex;
    align-items: center;
    gap: 6px;
  }
  .brand__dot {
    width: 26px;
    height: 26px;
    border-radius: 50%;
    background: var(--brand-navy);
    flex: none;
  }
  .brand__name {
    font-weight: 700;
    font-size: 8.5px;
    line-height: 1.15;
    color: var(--brand-navy);
    letter-spacing: 0.02em;
  }
  .card--back .brand { left: 42px; top: 170px; }
  .card--front .brand { left: 238px; top: 40px; }

  .services {
    position: absolute;
    right: 47px;
    top: 166px;
    list-style: none;
    text-align: right;
    font-size: 5.6px;
    line-height: 7.5px;
    letter-spacing: 0.06em;
    text-transform: uppercase;
    color: var(--ink-soft);
  }
  .services__rule {
    position: absolute;
    left: 370px;
    top: 162px;
    width: 1px;
    height: 44px;
    background: var(--rule);
  }

  .person { position: absolute; left: 40px; top: 41px; }
  .person__name {
    font-weight: 700;
    font-size: 22.5px;
    line-height: 19px;
    color: var(--ink);
  }
  .person__title {
    margin-top: 9px;
    font-size: 8px;
    color: var(--ink-soft);
  }
  .contact { position: absolute; left: 40px; top: 152px; }
  .contact__rule {
    width: 47px;
    height: 1px;
    background: var(--rule);
    margin-bottom: 9px;
  }
  .contact__line {
    font-size: 8.6px;
    line-height: 9.9px;
    color: var(--ink);
  }
  .slogan {
    position: absolute;
    right: 42px;
    top: 166px;
    text-align: right;
    font-weight: 700;
    font-style: italic;
    font-size: 7.6px;
    line-height: 10.5px;
    color: var(--ink);
  }
</style>
</head>
<body>
<main class="canvas">
  <section class="card card--back" aria-label="Card back">
    <div class="brand">
      <span class="brand__dot"></span>
      <span class="brand__name">Steadfast Upkeep<br>Industrial</span>
    </div>
    <ul class="services">
      <li>Routine Inspections</li>
      <li>Equipment Maintenance</li>
      <li>Emergency Repairs</li>
      <li>Consultation Services</li>
      <li>New Installs</li>
    </ul>
    <span class="services__rule"></span>
  </section>

  <section class="card card--front" aria-label="Card front">
    <div class="person">
      <h1 class="person__name">Darren<br>Whitlow</h1>
      <p class="person__title">Chief Executive Officer</p>
    </div>
    <div class="brand">
      <span class="brand__dot"></span>
      <span class="brand__name">Steadfast Upkeep<br>Industrial</span>
    </div>
    <div class="contact">
      <div class="contact__rule"></div>
      <p class="contact__line">0123 Name St. City, AA 12345</p>
      <p class="contact__line">Phone - (802)-5196-047</p>
      <p class="contact__line">darren@sukrn.com</p>
      <p class="contact__line">www.sukrn.com</p>
    </div>
    <p class="slogan">Keeping Your Equipment<br>Running Smoothly.</p>
  </section>
</main>
</body>
</html>
```